Stonebrook Aerial Business Card

We are a new company based in Central Queensland, Australia that uses specalised drones (Velkor Sprayhawk K40) to undertake mainly agricultural operations, like spraying weeds, spraying crops, spreading seed etc. I have attached a Plinto proof of a card I was thinking along the lines of - purely a start point. The drone used in the business card MUST be a Velkor Sprayhawk K40.
I am very open to other ideas, especially fonts and layout. I don't have website etc set up yet.
The images are stock and easily interchangeable, I just ask that any background images reflect the local central Queensland area. The photo of the drone is not even complete (propellers cut off) and I need a new stock photo – I’m not sure if this is an issue, or I can pay for an image if need be. PLEASE FIND AN SPRAYHAWK K40 image - 4 sprayers, not 6.
The logo/business name is very draft and looking for further ideas, ideally incorporating drones or agriculture design elements into the design of the business name. The business name needs work on the graphic/design – it is a draft that I have included, the drone propellers (being a different colour) are DRAFT only and intended for changes. PLEASE DO NOT USE THE DRONE PORPELLER I HAVE USED AS A DRAFT. TRY TO FIND SOMETHING ELSE.. The arrow is a shape and not aligned in any way, I would also like ideas on different fonts and additional elements, like air streams, aviation elements, aviation or country western (farming like) themes and fonts etc.
Ideally looking at staying within the blue, green and yellow colours, keeping with an natural, outdoorsy, environmental feel.

Target Market(s)

Farmers, Agriculture, Local Governments, Land Managers

Industry/Entity Type

Agriculture, Drones, Aviation

Contact Information for Business Card

Agricultural Drone (Velkor Sprayhawk K40), Farming, Business Name.

Font styles to use
Sans Serif

Colors
0054AA
0677BA
7BADD7
CADEEF
E8F1F8
0094D4
00A9DD
6FCCEA
C7EBF8
E9F6FB
00AB8E
00BBA5
67D7C9
C6EFE9
E9F9F6
59FF00
82FF00
B8FF75
E3FFCB
F4FFEA

Requirements
Must have
• Velkor Sprayhawk K40 Drone
Should not have
• Tractors

```html
<!DOCTYPE html>
<html lang="en">
<head>
<meta charset="utf-8">
<title>Stonebrook Aerial – Business Card</title>
<link rel="stylesheet" href="https://fonts.googleapis.com/css2?family=Exo+2:wght@700;800&family=Poppins:wght@400;600;700&display=swap">
<style>
  :root {
    --stage: #8f8f8f;
    --green: #3a9a0c;
    --green-bright: #48b312;
    --ink: #141414;
    --panel: #131313;
    --white: #ffffff;
    --sky: #a9cbe6;
    --hill: #4a7a2e;
    --field: #6aa73a;
    --drone: #8c8c8c;
  }
  * { margin: 0; padding: 0; box-sizing: border-box; }
  html, body { width: 998px; height: 1200px; overflow: hidden; background: var(--stage); }
  .card {
    position: absolute; left: 132px; width: 734px; height: 419px;
    background: var(--white); overflow: hidden;
    box-shadow: 0 3px 10px rgba(0,0,0,.25);
  }
  .card--front { top: 120px; }
  .card--back { top: 660px; }
  .card svg.shapes { position: absolute; inset: 0; }
  .services {
    position: absolute; left: 37px; top: 34px;
    font-family: "Exo 2", sans-serif; font-weight: 800;
    font-size: 29px; line-height: 35px; color: var(--ink);
    letter-spacing: .3px;
  }
  .services .verb { color: var(--green); }
  .brand {
    position: absolute; font-family: "Poppins", sans-serif;
    font-weight: 700; font-size: 26px; line-height: 1; letter-spacing: -.5px;
    white-space: nowrap;
  }
  .card--front .brand { left: 472px; top: 108px; color: var(--ink); }
  .card--back .brand { left: 350px; top: 110px; color: var(--white); }
  .holder {
    position: absolute; left: 380px; top: 180px;
    font-family: "Poppins", sans-serif; font-weight: 700; font-size: 26px; color: var(--white);
  }
  .holder .surname { color: var(--green-bright); }
  .role {
    position: absolute; left: 398px; top: 222px;
    font-family: "Poppins", sans-serif; font-weight: 600; font-size: 15px; color: var(--white);
  }
  .contacts { position: absolute; top: 306px; left: 420px; list-style: none;
    font-family: "Poppins", sans-serif; font-size: 15px; color: #222; }
  .contacts li { display: flex; align-items: center; gap: 6px; height: 24px; }
  .contacts li:nth-child(2) { margin-left: 14px; }
  .contacts li:nth-child(3) { margin-left: 29px; }
  .contacts svg { width: 18px; height: 18px; flex: none; }
</style>
</head>
<body>

<section class="card card--front">
  <svg class="shapes" width="734" height="419" viewBox="0 0 734 419">
    <defs>
      <linearGradient id="frontScene" x1="0" y1="0" x2="0" y2="1">
        <stop offset="0" stop-color="#ffffff"/>
        <stop offset=".3" stop-color="var(--sky)"/>
        <stop offset=".45" stop-color="var(--hill)"/>
        <stop offset=".75" stop-color="var(--field)"/>
        <stop offset=".9" stop-color="#b08a4a"/>
        <stop offset="1" stop-color="#7aa640"/>
      </linearGradient>
      <linearGradient id="frontMist" x1="0" y1="0" x2="1" y2="1">
        <stop offset="0" stop-color="#ffffff"/>
        <stop offset="1" stop-color="#ececec"/>
      </linearGradient>
    </defs>
    <rect width="734" height="419" fill="url(#frontMist)"/>
    <polygon role="img" aria-label="Central Queensland sugar cane field beneath green hills"
      points="0,0 348,0 455,209 334,419 0,419" fill="url(#frontScene)"/>
    <polygon points="348,0 460,0 404,92" fill="var(--green)"/>
    <polyline points="480,0 420,106 479,209 357,419" fill="none" stroke="var(--green)" stroke-width="1.5"/>
    <rect role="img" aria-label="Sprayhawk K40 agricultural spray drone in flight"
      x="480" y="175" width="250" height="230" rx="30" fill="var(--drone)" opacity=".35"/>
  </svg>
  <div class="services">
    <div><span class="verb">SPRAYING</span> WEEDS</div>
    <div><span class="verb">SPRAYING</span> CROPS</div>
    <div><span class="verb">SPREADING</span> SEED</div>
  </div>
  <div class="brand">Stonebrook Aerial</div>
</section>

<section class="card card--back">
  <svg class="shapes" width="734" height="419" viewBox="0 0 734 419">
    <defs>
      <linearGradient id="backScene" x1="0" y1="0" x2="0" y2="1">
        <stop offset="0" stop-color="#4c9be0"/>
        <stop offset=".45" stop-color="#c9e1f4"/>
        <stop offset=".58" stop-color="#2f6a22"/>
        <stop offset=".7" stop-color="#5bab2c"/>
        <stop offset="1" stop-color="#3d8a1e"/>
      </linearGradient>
      <linearGradient id="backMist" x1="0" y1="0" x2="1" y2="1">
        <stop offset="0" stop-color="#ffffff"/>
        <stop offset="1" stop-color="#e6e6e6"/>
      </linearGradient>
    </defs>
    <rect width="734" height="419" fill="url(#backMist)"/>
    <polygon role="img" aria-label="Green crop rows under a blue Queensland sky"
      points="0,17 233,17 334,185 194,419 0,419" fill="url(#backScene)"/>
    <polygon points="283,0 734,0 734,280 395,284 330,175 265,45" fill="var(--panel)"/>
    <polyline points="345,202 395,288 734,292" fill="none" stroke="var(--green)" stroke-width="1.5"/>
    <polyline points="345,202 220,419" fill="none" stroke="var(--green)" stroke-width="1.5"/>
    <line x1="487" y1="235" x2="734" y2="235" stroke="#bbbbbb" stroke-width="1"/>
    <polygon points="240,395 734,395 734,419 224,419" fill="var(--green)"/>
    <rect role="img" aria-label="Sprayhawk K40 agricultural spray drone in flight"
      x="195" y="292" width="205" height="100" rx="20" fill="var(--drone)" opacity=".45"/>
  </svg>
  <div class="brand">Stonebrook Aerial</div>
  <div class="holder">Mathieu <span class="surname">Arden</span></div>
  <div class="role">FOUNDER</div>
  <ul class="contacts">
    <li>
      <svg viewBox="0 0 18 18"><circle cx="9" cy="9" r="9" fill="var(--green)"/><path d="M6 4.5l2 2-1 1.2c.6 1.3 1.6 2.3 2.9 2.9l1.2-1 2 2-1.2 1.4c-3.5-.3-6.9-3.7-7.2-7.2z" fill="#fff"/></svg>
      <span>033 987654 321</span>
    </li>
    <li>
      <svg viewBox="0 0 18 18"><circle cx="9" cy="9" r="9" fill="var(--green)"/><rect x="4.5" y="6" width="9" height="6.5" fill="#fff"/><path d="M4.5 6l4.5 3.6L13.5 6" fill="none" stroke="var(--green)" stroke-width="1"/></svg>
      <span>@Stonebrook Aerial.com</span>
    </li>
    <li>
      <svg viewBox="0 0 18 18"><circle cx="9" cy="9" r="9" fill="var(--green)"/><g fill="none" stroke="#fff" stroke-width="1"><circle cx="9" cy="9" r="4.8"/><ellipse cx="9" cy="9" rx="2" ry="4.8"/><line x1="4.2" y1="9" x2="13.8" y2="9"/></g></svg>
      <span>www.Stonebrook Aerial.com</span>
    </li>
  </ul>
</section>

</body>
</html>
```